Group Medical Practice needs stationery, business cards etc. designed

We need stationery designed for a multisite practice that offers primary medical, dental and behavioral healthcare. We would like a design that is consistent for letterhead, business cards, Microsoft Outlook stationery etc. We have attached our new logo design.

```html
<!DOCTYPE html>
<html lang="en">
<head>
<meta charset="utf-8">
<title>Cedar Ridge Health Services – Stationery</title>
<link href="https://fonts.googleapis.com/css2?family=Open+Sans:ital,wght@0,400;0,600;1,400&display=swap" rel="stylesheet">
<style>
  :root {
    --bg: #e6e6e6;
    --paper: #ffffff;
    --green: #8cc63f;
    --blue: #2a7ab8;
    --text: #6a6a6a;
    --muted: #8a8a8a;
  }
  * { box-sizing: border-box; margin: 0; padding: 0; }
  html, body { width: 1200px; height: 1000px; overflow: hidden; }
  body {
    background: var(--bg);
    font-family: "Open Sans", Arial, sans-serif;
    color: var(--text);
    position: relative;
  }
  .sheet, .card {
    position: absolute;
    background: var(--paper);
    box-shadow: 0 2px 8px rgba(0,0,0,0.12);
  }
  .brand {
    display: flex;
    align-items: center;
    gap: 8px;
    color: var(--blue);
    font-weight: 600;
    white-space: nowrap;
  }
  .brand-dot {
    width: 12px; height: 12px; border-radius: 50%;
    background: var(--green);
    flex: none;
  }

  /* Letterhead */
  .letterhead { left: 80px; top: 112px; width: 600px; height: 776px; }
  .letterhead .brand { position: absolute; left: 40px; top: 56px; font-size: 17px; }
  .letterhead .rule-h {
    position: absolute; left: 30px; right: 0; top: 102px;
    height: 2px; background: var(--green);
  }
  .letterhead .rule-v {
    position: absolute; left: 392px; top: 30px; height: 92px;
    width: 2px; background: var(--green);
  }
  .letterhead .contact {
    position: absolute; left: 404px; top: 36px;
    font-size: 8.5px; line-height: 1.55; color: var(--muted);
  }
  .letterhead .contact b { font-weight: 600; color: var(--text); }
  .letter-body {
    position: absolute; left: 70px; top: 150px; width: 460px;
    font-size: 10.5px; line-height: 1.6;
  }
  .letter-body p { margin-bottom: 14px; }
  .signature { position: absolute; left: 400px; top: 625px; }
  .signature .name { color: var(--blue); font-weight: 600; font-size: 14px; }
  .signature .role { font-size: 10.5px; color: var(--muted); }

  /* Business cards */
  .card { width: 400px; height: 230px; }
  .card-back { left: 740px; top: 190px; }
  .card-back .brand {
    position: absolute; left: 0; right: 0; top: 100px;
    justify-content: center; font-size: 19px;
  }
  .card-front { left: 740px; top: 560px; }
  .card-front .brand { position: absolute; left: 24px; top: 28px; font-size: 13px; }
  .card-front .rule-h {
    position: absolute; left: 20px; right: 0; top: 96px;
    height: 2px; background: var(--green);
  }
  .card-front .rule-v {
    position: absolute; left: 196px; top: 96px; bottom: 0;
    width: 2px; background: var(--green);
  }
  .card-front .address {
    position: absolute; left: 26px; top: 110px;
    font-size: 8.5px; line-height: 1.6; color: var(--muted);
  }
  .card-front .person { position: absolute; left: 212px; top: 120px; }
  .card-front .name { color: var(--blue); font-weight: 600; font-size: 18px; }
  .card-front .role { font-size: 10px; color: var(--muted); }
</style>
</head>
<body>

  <section class="sheet letterhead">
    <div class="brand"><span class="brand-dot"></span>Cedar Ridge Health Services</div>
    <div class="rule-h"></div>
    <div class="rule-v"></div>
    <div class="contact">
      240 Larch Street Ste 14<br>
      Millbrook, Ohio 45021<br>
      <b>Phone</b> 555 014 2260<br>
      <b>Fax</b> 555 014 2261
    </div>

    <div class="letter-body">
      <p>Lorem ipsum dolor sit amet,</p>
      <p>Consectetur adipiscing elit. Mauris at vestibulum elit. Mauris sed malesuada turpis, nec lobortis mi. Proin nec lacus condimentum, mattis dolor nec, luctus enim. Nunc in nunc metus. Donec convallis diam mauris, quis eleifend odio tincidunt sed. Proin sed nulla aliquet, tincidunt est sit amet, eleifend ipsum. Aenean vitae maximus metus, at hendrerit enim. Donec cursus ante sed euismod tempor. Nam quis tortor varius, pellentesque tortor ac, porta mi. Integer lorem sem, mollis ac pulvinar ac, rutrum vitae massa. Nam ut mauris id tellus aliquam commodo. Proin iaculis turpis ut arcu ullamcorper, vel commodo mauris feugiat. Etiam finibus in nisl sit amet ultrices.</p>
      <p>Pellentesque non efficitur nibh. In sollicitudin accumsan velit. Cras mollis erat lectus, et ultrices felis vehicula sed. Proin odio libero, consectetur non felis quis, scelerisque fringilla urna. Cras venenatis rhoncus enim, id finibus nibh maximus ut. Morbi scelerisque laoreet tempor. Phasellus dignissim lectus et lacus interdum pulvinar. Ut pulvinar imperdiet massa, ac molestie magna cursus non. Duis diam erat, finibus ac imperdiet nec, gravida vel arcu. Pellentesque non rutrum nibh. Aenean tristique metus et libero ornare pretium. Nullam fermentum mollis vulputate.</p>
      <p>Vestibulum a pulvinar ante, auctor porttitor sapien. Fusce ornare, dolor posuere viverra scelerisque, lacus dui efficitur ante, non lacinia ligula ligula lacinia velit. Suspendisse finibus nulla ac vulputate tincidunt.</p>
    </div>

    <div class="signature">
      <div class="name">Daniel Hartwell</div>
      <div class="role">President and C.E.O</div>
    </div>
  </section>

  <section class="card card-back">
    <div class="brand"><span class="brand-dot"></span>Cedar Ridge Health Services</div>
  </section>

  <section class="card card-front">
    <div class="brand"><span class="brand-dot"></span>Cedar Ridge Health Services</div>
    <div class="rule-h"></div>
    <div class="rule-v"></div>
    <div class="address">
      240 Larch Street Ste 14<br>
      Millbrook, Ohio 45021
    </div>
    <div class="person">
      <div class="name">Daniel Hartwell</div>
      <div class="role">President and C.E.O</div>
    </div>
  </section>

</body>
</html>
```